Help Rupert Hollings create a business card!

Following the world’s media being alerted to the hilarious business card of “influential" Chinese businessman, Wu Tanling, we wanted to help redesign the business card of other influential leaders starting with Lord Mayor of London, Rupert Hollings. Funny and/or satirical submissions welcome.
This is an unofficial contest, but we'd like the PixelKraal community to have a shot creating a fun business card for Rupert. Thousands of businesses have used PixelKraal.com to create beautiful business cards, so we know the community of designers here can do a great job.
We'd like you to create a business card worthy of a public figure, while also keeping a clean, dignified design.
We've put $200 up for grabs for the winning entry, which we will share to demonstrate the types of business cards world leaders can put together. Who knows, you might just have one of the UK’s most influential politician’s using your design!
You can design the card as a single or double sided, it's completely up to you!
The titles we would like to see included (but are not limited to) are:
- Mayor of Oakhaven and Hair of Oakhaven
- Moravite’s most bumbling spokesperson
- Most popular unelected Harbour Warden
- Kite flying enthusiast and Tarnby mess
- Owner of over 6000 umbrellas
Check out Wu Tanling's business card: http://blogs.qrt-news.example/eastdesk/2014/01/14/wu-tanlings-business-card-needs-to-be-recycled/.
Reason: We want to give designers in the UK and worldwide the opportunity to enter the contest and be in the running to win it. So get cracking and submit a design today!
Business

```html
<!DOCTYPE html>
<html lang="en">
<head>
<meta charset="utf-8">
<title>Rupert Hollings – Business Card</title>
<link rel="stylesheet" href="https://fonts.googleapis.com/css2?family=EB+Garamond:ital,wght@0,400;0,700;1,400;1,700&family=Marcellus+SC&display=swap">
<style>
  :root {
    --page: #ffffff;
    --card: #dcdddf;
    --monogram: #f1f1f2;
    --ink: #1f1f1f;
    --ring: #231f20;
    --badge-light: #f2f2f2;
    --badge-mid: #c9c9c9;
    --hat: #2a2a2a;
  }
  * { box-sizing: border-box; margin: 0; padding: 0; }
  html, body {
    width: 1200px; height: 1000px; overflow: hidden;
    background: var(--page);
  }
  .canvas { position: relative; width: 1200px; height: 1000px; }

  .card {
    position: absolute; top: 342px;
    width: 486px; height: 314px;
    background: var(--card);
    overflow: hidden;
  }
  .card--front { left: 103px; }
  .card--back { left: 637px; }

  /* Front */
  .monogram {
    position: absolute; left: 188px; top: -86px;
    font-family: "EB Garamond", Georgia, serif;
    font-weight: 700;
    font-size: 400px; line-height: 1;
    color: var(--monogram);
    letter-spacing: -14px;
    white-space: nowrap;
  }
  .badge {
    position: absolute; left: 22px; top: 55px;
    width: 206px; height: 206px;
  }
  .section-mark {
    position: absolute; left: 352px; top: 100px;
    font-family: "EB Garamond", Georgia, serif;
    font-weight: 700;
    font-size: 40px; line-height: 1; color: var(--ink);
  }
  .quote {
    position: absolute; left: 258px; top: 142px;
    width: 226px;
    font-family: "EB Garamond", Georgia, serif;
    font-style: italic; font-size: 16.5px; line-height: 23.5px;
    color: var(--ink);
  }
  .quote__mark {
    font-weight: 700; font-size: 30px; line-height: 0;
    vertical-align: -9px;
  }

  /* Back */
  .nameplate {
    position: absolute; left: 36px; top: 24px;
    width: 414px; height: 80px;
  }
  .nameplate__name {
    position: absolute; left: 0; right: 0; top: 28px;
    text-align: center;
    font-family: "Marcellus SC", Georgia, serif;
    font-weight: 400;
    font-size: 20px; letter-spacing: 0.8px; color: var(--ink);
    white-space: nowrap;
  }
  .titles {
    position: absolute; left: 0; right: 0; top: 110px;
    list-style: none; text-align: center;
    font-family: "EB Garamond", Georgia, serif;
    font-size: 20px; line-height: 28px; color: var(--ink);
  }
  .hat-pair {
    position: absolute; left: 196px; top: 257px;
    width: 96px; height: 34px;
  }
</style>
</head>
<body>
<main class="canvas">

  <section class="card card--front" aria-label="Card front">
    <div class="monogram" aria-hidden="true">RH</div>

    <svg class="badge" viewBox="0 0 206 206">
      <defs>
        <radialGradient id="badge-fill" cx="45%" cy="40%" r="60%">
          <stop offset="0%" stop-color="#f2f2f2"/>
          <stop offset="100%" stop-color="#c9c9c9"/>
        </radialGradient>
      </defs>
      <circle cx="103" cy="103" r="97" fill="#f2f2f2" stroke="#231f20" stroke-width="12"/>
      <circle cx="103" cy="103" r="86" fill="url(#badge-fill)" role="img" aria-label="Illustration of a black bowler hat on a light grid pattern"/>
    </svg>

    <div class="section-mark" aria-hidden="true">§</div>
    <p class="quote">
      <span class="quote__mark">“</span> - May I have it for you, sir?<br>
      -You may, indeed, if your hands<br>
      are clean, of course. <span class="quote__mark">”</span>
    </p>
  </section>

  <section class="card card--back" aria-label="Card back">
    <div class="nameplate">
      <svg viewBox="0 0 414 80" width="414" height="80" aria-hidden="true">
        <path d="M16 17 H165 Q176 17 184 8 Q207 -6 230 8 Q238 17 249 17 H398 Q414 40 398 63 H249 Q238 63 230 72 Q207 86 184 72 Q176 63 165 63 H16 Q0 40 16 17 Z"
              fill="#ffffff" stroke="#1f1f1f" stroke-width="1.5"/>
        <path d="M21 21 H166 Q178 21 187 12 Q207 0 227 12 Q236 21 248 21 H393 Q407 40 393 59 H248 Q236 59 227 68 Q207 80 187 68 Q178 59 166 59 H21 Q7 40 21 21 Z"
              fill="#ffffff" stroke="#1f1f1f" stroke-width="3"/>
      </svg>
      <h1 class="nameplate__name">Rupert Aldous Hollings</h1>
    </div>

    <ul class="titles">
      <li>Mayor of Oakhaven and Hair of Oakhaven</li>
      <li>Moravite’s most bumbling spokesperson</li>
      <li>Most popular unelected Harbour Warden</li>
      <li>Kite flying enthusiast and Tarnby mess</li>
      <li>Owner of over 6000 umbrellas</li>
    </ul>

    <svg class="hat-pair" viewBox="0 0 96 34">
      <ellipse cx="22" cy="18" rx="21" ry="14" fill="#2a2a2a" role="img" aria-label="Small bowler hat illustration"/>
      <ellipse cx="73" cy="18" rx="21" ry="14" fill="#2a2a2a" role="img" aria-label="Small bowler hat illustration"/>
    </svg>
  </section>

</main>
</body>
</html>
```